One of a kind, 100% Pure & Natural Skincare line needs stunning product label

We need product label design for new natural skincare company called Milo & Tess Skincare. We create luxurious, 100% pure & natural skincare that is free from ingredients that may be potentially irritating to the skin. No toxins, preservatives or additives. Our initial product is Harbor Glow Balm, a nourishing face cream that suits discerning women with mature skin and those with dry/sensitive skin needing extra hydration. Also those that choose to minimize their exposure to environmental toxins. Our brand is simple yet elegant, supporting a holistic, authentic lifestyle and Nurturing Gentle Skincare.

Target Market(s)

Discerning women with mature skin and those with dry/sensitive skin needing extra hydration. Also those that choose to minimize their exposure to environmental toxins.

Industry/Entity Type

Skin Care Product

Font styles to use
Sans Serif
Script

Colors
f9d9e8
fef1ee

Requirements
Must have
• The Logo.
HARBOR GLOW BALM
NURTURING GENTLE SKINCARE
Labels must be feminine, simple/minimal yet stylish. Uncluttered yet elegant.
This is a very natural product with minimal ingredients.
Nice to have
• The logo can be incorporated in to the label, or It can be left separate as a sticker on top of the jar. The product is a firm balm consistency and is in frosted glass jars with matt silver lids.
Jar height is 45mm, width is 60mm.
Label height: 28mm and length 185mm
Should not have
• Natural or farmers market type theme. No Bold/loud lettering.

```html
<!DOCTYPE html>
<html lang="en">
<head>
<meta charset="UTF-8">
<title>Harbor Glow Balm – Label</title>
<link rel="stylesheet" href="https://fonts.googleapis.com/css2?family=Raleway:wght@200;300&display=swap">
<style>
  :root {
    --page-bg: #f4f4f4;
    --label-pink: #d8687f;
    --label-pink-deep: #cf5d75;
    --tree-glow: #e89aab;
    --ink-light: #fbeef1;
  }
  html, body {
    margin: 0;
    padding: 0;
    width: 1200px;
    height: 703px;
    overflow: hidden;
    background: var(--page-bg);
  }
  .canvas {
    position: relative;
    width: 1200px;
    height: 703px;
  }
  .label {
    position: absolute;
    left: 100px;
    top: 156px;
    width: 1000px;
    height: 390px;
    background: linear-gradient(180deg, var(--label-pink) 0%, var(--label-pink-deep) 100%);
    overflow: hidden;
  }
  .label__tree {
    position: absolute;
    left: 0;
    top: 0;
    width: 440px;
    height: 390px;
  }
  .label__text {
    position: absolute;
    left: 282px;
    top: 166px;
    font-family: "Raleway", sans-serif;
    color: var(--ink-light);
  }
  .product-name {
    margin: 0;
    font-weight: 300;
    font-size: 70px;
    line-height: 0.98;
    letter-spacing: 2px;
    text-transform: uppercase;
  }
  .divider {
    width: 88px;
    height: 2px;
    margin: 12px 0 10px;
    background: var(--ink-light);
  }
  .tagline {
    margin: 0;
    font-weight: 200;
    font-size: 32px;
    letter-spacing: 0.5px;
  }
</style>
</head>
<body>
  <main class="canvas">
    <section class="label">
      <svg class="label__tree" viewBox="0 0 440 390" role="img" aria-label="Soft pink tree illustration spreading its branches over the label">
        <defs>
          <radialGradient id="treeGlow" cx="50%" cy="45%" r="55%">
            <stop offset="0%" stop-color="#e89aab" stop-opacity="0.75"/>
            <stop offset="100%" stop-color="#e89aab" stop-opacity="0"/>
          </radialGradient>
        </defs>
        <rect width="440" height="390" fill="url(#treeGlow)"/>
      </svg>
      <div class="label__text">
        <h1 class="product-name">Harbor<br>Glow Balm</h1>
        <div class="divider"></div>
        <p class="tagline">Nurturing Gentle Skincare</p>
      </div>
    </section>
  </main>
</body>
</html>
```